US Higher Education Changes Infographic

Create an info graphic which visually demonstrates statistics from and industry study of college students/parents and higher education professionals.

This graphic should be visually pleasing and conform with our brand styles.

Illustrations/icons should not be too juvenile or cartoon

We prefer a vibrant crisp design and is impactful and not cluttered.

examples are attached for reference.

Target Market(s)

US higher education industry

Industry/Entity Type

College

Requirements
Must have
• 8x10 finished design
• use colors and fonts from style guide
Should not have
• cluttered design, juvenile images

```html
<!DOCTYPE html>
<html lang="en">
<head>
<meta charset="utf-8">
<title>The FAFSA Opens Early</title>
<link rel="stylesheet" href="https://fonts.googleapis.com/css2?family=Questrial&family=Montserrat:wght@600;700&display=swap">
<style>
  :root {
    --green: #6cbd45;
    --orange: #f7941d;
    --grey: #6d6e71;
    --grey-light: #bcbec0;
    --ink: #58595b;
    --white: #ffffff;
  }
  * { box-sizing: border-box; margin: 0; padding: 0; }
  html, body { width: 848px; height: 1200px; overflow: hidden; background: var(--white); }
  body { font-family: "Questrial", sans-serif; color: var(--ink); }
  .canvas { position: relative; width: 848px; height: 1200px; }
  .abs { position: absolute; }
  .heading { font-family: "Montserrat", sans-serif; font-weight: 700; }

  .title { left: 102px; top: 22px; font-size: 40px; color: var(--green); font-family: "Montserrat", sans-serif; font-weight: 600; }
  .title-rule { left: 102px; top: 70px; width: 432px; height: 1px; background: var(--grey); }
  .subtitle { left: 102px; top: 74px; width: 440px; font-size: 21px; line-height: 27px; color: var(--grey); }
  .brand { left: 590px; top: 64px; display: flex; align-items: center; gap: 10px; }
  .brand-dot { width: 26px; height: 26px; border-radius: 50%; background: var(--green); }
  .brand-name { font-size: 30px; color: var(--ink); }

  .banner { display: flex; align-items: center; justify-content: center; color: var(--white); }
  .banner-green { left: 24px; top: 164px; width: 800px; height: 64px; background: var(--green); border-radius: 40px 40px 0 0; font-size: 32px; }
  .banner-grey { left: 24px; top: 594px; width: 800px; height: 64px; background: var(--grey); border-radius: 40px; font-size: 37px; }
  .tab { width: 24px; height: 64px; }
  .tab-left { border-radius: 0 0 0 24px; }
  .tab-right { border-radius: 0 0 24px 0; }

  .pictograph { display: flex; gap: 4px; }
  .unit { flex: 1; border-radius: 6px 6px 2px 2px; background: var(--grey-light); }
  .unit.on { background: var(--orange); }

  .stat { font-family: "Montserrat", sans-serif; font-weight: 700; color: var(--orange); }
  .copy { font-size: 14px; line-height: 17px; color: var(--ink); }
  .section-head { font-family: "Montserrat", sans-serif; font-weight: 700; font-size: 18px; color: var(--green); }
  .rule-h { height: 1px; background: var(--green); }
  .rule-v { width: 1px; background: var(--green); }
  .dash-h { border-top: 1px dashed var(--grey); }
  .dash-v { border-left: 2px dotted var(--grey); }

  .art { border-radius: 10px; }
  .art-grey { background: linear-gradient(135deg, #77787b, #5d5e61); }
  .art-mix { background: linear-gradient(135deg, var(--orange), var(--grey)); }
  .art-green { background: linear-gradient(135deg, var(--green), var(--grey)); }

  .hl { color: var(--green); }
  .result { left: 574px; top: 674px; font-size: 27px; line-height: 32px; color: var(--green); }

  .band { left: 22px; top: 758px; width: 804px; height: 60px; background: var(--green); display: flex; align-items: center; justify-content: space-around; color: var(--white); font-size: 15px; }
  .band-fold { width: 22px; height: 12px; background: #4f9a30; }

  .practices { left: 128px; top: 992px; width: 580px; height: 42px; background: var(--orange); border-radius: 0 0 36px 36px; font-size: 26px; color: var(--white); }
</style>
</head>
<body>
<div class="canvas">
  <h1 class="abs title">The FAFSA Opens Early</h1>
  <div class="abs title-rule"></div>
  <p class="abs subtitle">The class of 2017 will begin filing their FAFSA on October 1st using income and tax data from 2015</p>
  <div class="abs brand"><span class="brand-dot"></span><span class="brand-name">Lumora</span></div>

  <h2 class="abs banner banner-green heading">WHAT ARE STUDENTS AND FAMILIES SAYING?</h2>
  <div class="abs tab tab-left" style="left:24px;top:232px;background:var(--green)"></div>
  <div class="abs tab tab-right" style="left:800px;top:232px;background:var(--green)"></div>
  <div class="abs tab tab-left" style="left:24px;top:520px;background:var(--grey);border-radius:24px 0 0 0"></div>
  <div class="abs tab tab-right" style="left:800px;top:520px;background:var(--grey);border-radius:0 24px 0 0"></div>

  <!-- cost factor -->
  <div class="abs pictograph" style="left:118px;top:244px;width:218px;height:42px">
    <span class="unit on"></span><span class="unit on"></span><span class="unit on"></span><span class="unit on"></span><span class="unit on"></span><span class="unit on"></span><span class="unit on"></span><span class="unit" style="background:linear-gradient(90deg,var(--orange) 60%,var(--grey-light) 60%)"></span><span class="unit"></span><span class="unit"></span>
  </div>
  <p class="abs copy" style="left:123px;top:294px;width:200px">Of Students who plan to aid for financial aid</p>
  <div class="abs dash-h" style="left:122px;top:330px;width:218px"></div>
  <div class="abs stat" style="left:120px;top:334px;font-size:30px">76%</div>
  <p class="abs copy" style="left:188px;top:336px;width:190px">indicated that cost was an important factor in the college selection process.</p>
  <div class="abs rule-h" style="left:50px;top:396px;width:358px"></div>
  <div class="abs rule-v" style="left:408px;top:232px;height:352px"></div>
  <p class="abs copy" style="left:111px;top:406px;width:290px;color:var(--orange)">More specifically, students and families want:</p>

  <h3 class="abs section-head" style="left:128px;top:454px">EARLIER UNDERSTANDING</h3>
  <div class="abs art art-grey" style="left:120px;top:480px;width:116px;height:84px" role="img" aria-label="Money bag with a figure and clock"></div>
  <div class="abs stat" style="left:182px;top:480px;font-size:30px">69%</div>
  <p class="abs copy" style="left:252px;top:481px;width:130px">believe an earlier understanding of cost and aid would be helpful to their planning process</p>

  <!-- award letter -->
  <h3 class="abs section-head" style="left:466px;top:244px">EARLIER AWARD LETTER DELIVERY</h3>
  <div class="abs pictograph" style="left:514px;top:276px;width:156px;height:28px">
    <span class="unit on"></span><span class="unit on"></span><span class="unit on"></span><span class="unit on"></span><span class="unit on"></span><span class="unit on"></span><span class="unit on"></span><span class="unit on"></span><span class="unit" style="background:linear-gradient(90deg,var(--orange) 90%,var(--grey-light) 90%)"></span><span class="unit"></span>
  </div>
  <div class="abs art art-mix" style="left:416px;top:324px;width:92px;height:68px" role="img" aria-label="Award letter being signed beside a clock"></div>
  <div class="abs stat" style="left:514px;top:310px;font-size:26px">89%</div>
  <p class="abs copy" style="left:568px;top:310px;width:150px">want their award letter earlier</p>
  <div class="abs dash-h" style="left:560px;top:346px;width:180px"></div>
  <div class="abs pictograph" style="left:514px;top:356px;width:156px;height:28px">
    <span class="unit on"></span><span class="unit on"></span><span class="unit on"></span><span class="unit on"></span><span class="unit" style="background:linear-gradient(90deg,var(--orange) 10%,var(--grey-light) 10%)"></span><span class="unit"></span><span class="unit"></span><span class="unit"></span><span class="unit"></span><span class="unit"></span>
  </div>
  <div class="abs stat" style="left:514px;top:386px;font-size:26px">41%</div>
  <p class="abs copy" style="left:566px;top:390px;width:196px">want their award letter in the fall semester of their Senior Year</p>
  <div class="abs rule-h" style="left:408px;top:445px;width:384px"></div>

  <h3 class="abs section-head" style="left:484px;top:454px">MORE TRANSPARENCY</h3>
  <div class="abs art art-grey" style="left:484px;top:480px;width:112px;height:88px" role="img" aria-label="College building under a magnifying glass"></div>
  <div class="abs stat" style="left:608px;top:476px;font-size:30px">82%</div>
  <p class="abs copy" style="left:608px;top:510px;width:172px;font-size:14.5px">would think more positively about a college that provided earlier insight</p>

  <h2 class="abs banner banner-grey heading">HOW ARE COLLEGES RESPONDING?</h2>

  <div class="abs art art-grey" style="left:94px;top:668px;width:88px;height:62px" role="img" aria-label="College building"></div>
  <p class="abs" style="left:206px;top:674px;font-size:19px;color:var(--grey)">Of the colleges polled in this study,</p>
  <div class="abs stat" style="left:206px;top:700px;font-size:24px">89%</div>
  <p class="abs copy" style="left:261px;top:700px;width:300px;font-size:13px;line-height:16px">think changes will have a <span class="hl">significant</span> or <span class="hl">VERY significant</span> impact on the admissions cycle.</p>
  <div class="abs rule-v" style="left:564px;top:678px;height:52px;background:var(--grey)"></div>
  <p class="abs result">AS A RESULT,<br>COLLEGES ARE:</p>

  <div class="abs band heading">
    <span>PLANNING TO CHANGE</span><span>DELIVERING EARLIER INSIGHTS</span><span>CONSEQUENCES OF INACTION</span>
  </div>
  <div class="abs band-fold" style="left:22px;top:818px;clip-path:polygon(0 0,100% 0,100% 100%)"></div>
  <div class="abs band-fold" style="left:804px;top:818px;clip-path:polygon(0 0,100% 0,0 100%)"></div>

  <div class="abs art art-green" style="left:60px;top:836px;width:92px;height:84px" role="img" aria-label="College building with change arrows"></div>
  <div class="abs stat" style="left:158px;top:826px;font-size:30px">68%</div>
  <p class="abs copy" style="left:158px;top:864px;width:110px">plan to make significant changes as a result of PPY and early FAFSA in 2016.</p>
  <div class="abs dash-v" style="left:276px;top:820px;height:160px"></div>

  <div class="abs art art-mix" style="left:292px;top:856px;width:84px;height:84px" role="img" aria-label="Hand holding an aid document with a clock"></div>
  <div class="abs stat" style="left:389px;top:826px;font-size:30px">77%</div>
  <p class="abs copy" style="left:389px;top:864px;width:120px">plan to shift their delivery of financial aid eligibility information earlier</p>
  <div class="abs dash-v" style="left:524px;top:820px;height:160px"></div>

  <div class="abs art art-green" style="left:538px;top:840px;width:102px;height:76px" role="img" aria-label="College building with thumbs down"></div>
  <div class="abs stat" style="left:642px;top:826px;font-size:30px">80%</div>
  <p class="abs copy" style="left:645px;top:866px;width:150px">believe that institutions that DO NOT shift their cycle earlier will be at a competitive disadvantage</p>

  <h2 class="abs banner practices heading">EMERGING BEST PRACTICES</h2>

  <div class="abs art art-mix" style="left:40px;top:1048px;width:72px;height:96px" role="img" aria-label="Presenter with audience and clock"></div>
  <p class="abs copy" style="left:133px;top:1068px;width:140px">Address ‘the cost question’ earlier in outreach and nurturing campaigns.</p>
  <div class="abs dash-v" style="left:298px;top:1060px;height:100px"></div>

  <div class="abs art art-grey" style="left:320px;top:1064px;width:84px;height:80px" role="img" aria-label="Balance scale weighing cost and value"></div>
  <p class="abs copy" style="left:421px;top:1068px;width:110px">Communicate cost alongside personalized value content</p>
  <div class="abs dash-v" style="left:540px;top:1060px;height:100px"></div>

  <div class="abs art art-grey" style="left:556px;top:1072px;width:84px;height:72px" role="img" aria-label="Two people in conversation"></div>
  <p class="abs copy" style="left:645px;top:1064px;width:150px">Extend communications programs to nurture relationships with prospective students along the way.</p>
</div>
</body>
</html>
```